Product Insert / Thank You

I'm looking for a small card to be designed that will be included with our product when it ships. It will be 2 sided with 1 side being a "thank you" with our logo and the other side containing the following text:We would love to hear your feedback! For every review we receive on our products, we donate 100% of the proceeds of your order to TIDEWELL -- a non profit organization dedicated to preserving our oceans!If you are not 100% satisfied with your purchase or have any problems, we will always resolve your issue. please contact us via Brisko if you need assistance.Insert needs to be well organized and information presented in a clear and visually appealing way.
Target Market(s)
Women, aged 24-45
Colors
Designer to choose colors to be used in the design.
Look and feel
Each slider illustrates characteristics of the customer's brand and the style your logo design should communicate.

```html
<!DOCTYPE html>
<html lang="en">
<head>
<meta charset="utf-8">
<title>Summitra Thank You Insert</title>
<link rel="stylesheet" href="https://fonts.googleapis.com/css2?family=Mrs+Saint+Delafield&family=PT+Sans:wght@400;700&display=swap">
<style>
  :root {
    --paper: #ffffff;
    --ink: #000000;
    --canvas: #ffffff;
    --card-shadow: rgba(0, 0, 0, 0.45);
  }
  * { margin: 0; padding: 0; box-sizing: border-box; }
  html, body {
    width: 1200px;
    height: 1200px;
    overflow: hidden;
    background: var(--canvas);
  }
  .canvas {
    position: relative;
    width: 1200px;
    height: 1200px;
    font-family: "PT Sans", sans-serif;
    color: var(--ink);
  }
  .card {
    position: absolute;
    width: 848px;
    height: 562px;
    background: var(--paper);
    box-shadow: 3px 4px 6px var(--card-shadow);
  }
  .card--back {
    left: 258px;
    top: 534px;
  }
  .card--front {
    left: 74px;
    top: 99px;
  }
  .back-band {
    position: absolute;
    left: 0;
    top: 0;
    width: 100%;
    height: 214px;
    background: var(--ink);
  }
  .feedback {
    position: absolute;
    left: 88px;
    top: 290px;
    width: 680px;
  }
  .feedback__title {
    font-size: 36px;
    font-weight: 700;
    letter-spacing: -0.4px;
    line-height: 1;
    white-space: nowrap;
  }
  .feedback__body {
    margin-top: 22px;
    font-size: 22px;
    line-height: 30px;
  }
  .feedback__line {
    display: block;
    white-space: nowrap;
    text-align: justify;
    text-align-last: justify;
  }
  .feedback__body strong { font-weight: 700; }
  .brand {
    position: absolute;
    left: 44px;
    top: 86px;
    display: flex;
    align-items: center;
    gap: 10px;
  }
  .brand__dot {
    width: 28px;
    height: 28px;
    border: 3px solid var(--ink);
    border-radius: 50%;
  }
  .brand__name {
    font-size: 24px;
    font-weight: 700;
    letter-spacing: 1px;
  }
  .thank-you {
    position: absolute;
    left: 60px;
    top: 190px;
    width: 700px;
    height: 290px;
    display: flex;
    align-items: center;
    justify-content: center;
    font-family: "Mrs Saint Delafield", cursive;
    font-weight: 400;
    font-size: 230px;
    line-height: 1;
    white-space: nowrap;
    transform: rotate(-4deg);
  }
</style>
</head>
<body>
  <main class="canvas">
    <section class="card card--back">
      <div class="back-band"></div>
      <div class="feedback">
        <h2 class="feedback__title">WE WOULD LOVE TO HEAR YOUR FEEDBACK!</h2>
        <p class="feedback__body">
          <span class="feedback__line">For every review we receive on our products, we donate 100% of</span>
          <span class="feedback__line">the proceed of your order to “<strong>TIDEWELL</strong>”- &nbsp;a non profit organization</span>
          <span class="feedback__line">dedicated to preserving our oceans ! If you’re not 100% satisfied</span>
          <span class="feedback__line">with your purchase or have any problems, we will always resolve</span>
          <span class="feedback__line">your issue. Please contact us via Brisko if you need assistance.</span>
        </p>
      </div>
    </section>
    <section class="card card--front">
      <div class="brand">
        <span class="brand__dot"></span>
        <span class="brand__name">SUMMITRA</span>
      </div>
      <h1 class="thank-you">Thank you!</h1>
    </section>
  </main>
</body>
</html>
```